COMPETITION TITLE:
Premium Skincare Packaging Design for Modern Hydration Beauty Brand
ABOUT THE PROJECT
We are developing a new skincare brand called VELORENA.
We are looking for a sophisticated and commercially strong packaging design direction for our initial skincare soft launch.
The brand positioning is:
* modern premium skincare
* hydration-focused
* wellness-oriented
* calming and elegant
* emotionally reassuring
* modern feminine skincare
* premium online beauty brand
The products are designed around hydration, skin comfort and modern skincare rituals.
The brand is inspired by modern hydration and skin wellness for people adapting between warmer and colder climates. The visual direction should therefore feel emotionally warm, comforting and restorative while remaining modern, refined and internationally premium rather than overtly cultural or decorative.
WHAT WE NEED
We are primarily seeking the VISUAL DIRECTION and PACKAGING IDENTITY for one hero product:
LIGHT MOISTURISING DAY CREAM
The winning visual direction will later be adapted across additional products within the range, including:
* Brightening Eye Cream
* Hydrating Mist / Toner
Therefore we are looking for a cohesive skincare brand identity system rather than unrelated individual designs.
IMPORTANT PACKAGING INFORMATION
The product packaging is:
* white plastic pump dispenser bottle
* transparent clear plastic lid
* outer cardboard carton/box
Bottle dimensions:
* diameter: 30mm
* total height including lid: 147mm
* bottle body height: approx. 120mm
* transparent lid height: approx. 27mm
Outer carton dimensions:
* height: 150mm
* width: 40mm x 35mm
IMPORTANT:
The packaging itself is minimalist and lightweight, therefore the LABEL DESIGN and OVERALL BRAND DIRECTION should visually elevate the product and make it feel:
* premium
* substantial
* calming
* elegant
* modern
* trustworthy
* emotionally warm
* intentional
The design should help the packaging feel significantly more premium than standard mass-market skincare.
FILES PROVIDED
We are providing:
* bottle label template
* outer box template
* logo/icon
* packaging dimensions
The supplied logo/icon should be retained conceptually, however designers may professionally refine and recreate/vectorise the artwork where required for packaging consistency and premium presentation.
At this stage we are NOT looking for final technical production artwork.
We are primarily looking for:
* visual direction
* typography
* colour palette
* premium skincare aesthetic
* realistic product mockups
IMPORTANT WEBSITE NOTE
A current website link may be provided for background information only.
Please DO NOT take heavy visual inspiration from the existing website design, as the website itself is expected to evolve in the future alongside the packaging direction.
The packaging design should therefore LEAD the future visual identity of the brand rather than follow the current website styling.
DESIGN STYLE
We are looking for:
* modern premium wellness skincare
* understated luxury
* elegant typography
* emotionally warm but clean branding
* hydration-focused beauty aesthetic
* premium online skincare look
The product should feel:
* calming when held
* emotionally reassuring rather than clinical
* modern wellness rather than minimalist pharmacy
* elegant but human rather than cold luxury
* comforting and restorative rather than cosmetic-only
Subtle texture, tonal layering and sophisticated visual depth are encouraged where appropriate.
Designers are encouraged to create a recognisable and distinctive visual identity rather than generic minimalist skincare packaging.
PLEASE AVOID
* gold luxury clichés
* ornate decorative themes
* floral overload
* influencer-style beauty branding
* overly clinical pharmacy aesthetics
* generic Canva-style layouts
* packaging that feels cold or sterile
STYLE REFERENCES
Please take inspiration from brands such as:
* Mirven
* Plume Beauty
* Coraval
* Beauty of Dallith
We particularly like:
* elegant spacing
* clean premium typography
* calm colour palettes
* subtle luxury
* modern hydration skincare aesthetics
COLOUR DIRECTION
Preferred tones include:
* warm ivory
* soft cream
* muted blush
* sand
* charcoal typography
* subtle deep plum accents
* restrained muted rose-gold accents
Please avoid:
* neon colours
* excessive metallic effects
* harsh black-and-white pharmacy styling
* very dark packaging
IMPORTANT DESIGN NOTE
The slim vertical packaging should feel intentionally elegant and premium rather than small or sample-sized.
The label design should visually elongate and elevate the packaging.
LOGO
An existing logo/icon is provided and should be retained and integrated into the design direction rather than completely redesigned.
DELIVERABLES
We are looking for:
* one fully developed hero product design
* realistic bottle + outer box mockups
* coordinated visual direction suitable for future product extensions
* typography and colour direction
* editable source files
The final approved visual system will later be adapted across additional products within the range.
BRAND NAME
VELORENA
OPTIONAL TAGLINE DIRECTION
Tideshift Balance Hydration
Updates
Thank you everyone for the submissions so far — there are some very strong directions emerging.
A few important thoughts as the project develops:
We are looking not only for attractive skincare labels, but for a distinctive and recognisable BRAND IDENTITY that could grow with the business over time across future packaging formats including larger cartons, jars and premium skincare packaging.
One area we would particularly encourage designers to explore further is refinement/elevation of the existing logo/icon. We would like to retain the core rose/circle concept, however subtle refinement, balance, geometry, typography pairing and premium presentation are encouraged where appropriate.
The strongest directions for us so far are those that feel:
* emotionally warm rather than clinical
* modern premium wellness rather than generic minimal skincare
* calming and reassuring when viewed or held
* elegant and distinctive rather than trend-driven
* premium without relying on gold luxury clichés
We are especially interested in designs that create a memorable visual identity system rather than simply placing text onto a white skincare bottle.
Subtle tonal layering, refined typography, understated sophistication and intelligent visual restraint are all encouraged.
Many thanks again and we are very excited to see the next round of directions develop.

```html
<!DOCTYPE html>
<html lang="en">
<head>
<meta charset="utf-8">
<title>VELORENA — Light Moisturising Cream Labels</title>
<link href="https://fonts.googleapis.com/css2?family=Cormorant+Garamond:wght@300;400;500&display=swap" rel="stylesheet">
<style>
  :root {
    --ivory: #f8f1ea;
    --blush: #e4c7c0;
    --blush-deep: #dcbcb4;
    --charcoal: #55504f;
    --rule: #b89f99;
    --mauve-band: #9b8886;
    --band-text: #ead9d4;
    --gold: #c9a24a;
  }
  * { margin: 0; padding: 0; box-sizing: border-box; }
  html, body {
    width: 1200px;
    height: 1200px;
    overflow: hidden;
    background: var(--ivory);
  }
  .canvas {
    position: relative;
    width: 1200px;
    height: 1200px;
  }
  .label {
    position: absolute;
    display: block;
  }
  .label--bottle { left: 351px; top: 407px; width: 157px; height: 637px; }
  .label--carton { left: 609px; top: 125px; width: 240px; height: 949px; }
  .label-ground { fill: url(#blushTone); }
  .product-title {
    font-family: "Cormorant Garamond", serif;
    font-weight: 500;
    fill: var(--charcoal);
  }
  .product-scent {
    font-family: "Cormorant Garamond", serif;
    font-weight: 500;
    fill: var(--charcoal);
  }
  .title-rule { stroke: var(--rule); stroke-width: 1; }
  .brand-mark { fill: none; stroke: var(--gold); }
  .wordmark {
    font-family: "Cormorant Garamond", serif;
    font-weight: 300;
    fill: var(--gold);
  }
  .volume-band { fill: var(--mauve-band); }
  .volume-text {
    font-family: "Cormorant Garamond", serif;
    font-weight: 500;
    fill: var(--band-text);
  }
</style>
</head>
<body>
<main class="canvas">

  <svg width="0" height="0" style="position:absolute" aria-hidden="true">
    <defs>
      <linearGradient id="blushTone" x1="0" y1="0" x2="1" y2="1">
        <stop offset="0" stop-color="#e6cac3"/>
        <stop offset="1" stop-color="#dfc1b9"/>
      </linearGradient>
      <clipPath id="bottleClip"><rect width="224" height="910" rx="12"/></clipPath>
      <clipPath id="cartonClip"><rect width="343" height="1355" rx="14"/></clipPath>
    </defs>
  </svg>

  <!-- Bottle label -->
  <svg class="label label--bottle" viewBox="0 0 224 910" aria-label="VELORENA Light Moisturising Cream bottle label">
    <g clip-path="url(#bottleClip)">
      <rect class="label-ground" width="224" height="910"/>
      <text class="product-title" x="34" y="42" font-size="19" letter-spacing="1.2">LIGHT</text>
      <text class="product-title" x="34" y="62" font-size="19" letter-spacing="1.2">MOISTURISING</text>
      <text class="product-title" x="34" y="82" font-size="19" letter-spacing="1.2">CREAM</text>
      <line class="title-rule" x1="34" y1="94" x2="196" y2="94"/>
      <text class="product-scent" x="34" y="115" font-size="13.5" letter-spacing="1">CITRUS &amp; GREEN TEA</text>
      <circle class="brand-mark" cx="120" cy="187" r="40" stroke-width="2"/>
      <text class="wordmark" transform="translate(153,807) rotate(-90)" font-size="92" textLength="560" lengthAdjust="spacing">VELORENA</text>
      <rect class="volume-band" x="0" y="852" width="224" height="58"/>
      <text class="volume-text" x="112" y="887" font-size="17" text-anchor="middle">50ml / 1.7 Fl. Oz.</text>
    </g>
  </svg>

  <!-- Carton front panel -->
  <svg class="label label--carton" viewBox="0 0 343 1355" aria-label="VELORENA Light Moisturising Cream carton front">
    <g clip-path="url(#cartonClip)">
      <rect class="label-ground" width="343" height="1355"/>
      <text class="product-title" x="24" y="65" font-size="30" letter-spacing="1.8">LIGHT</text>
      <text class="product-title" x="24" y="97" font-size="30" letter-spacing="1.8">MOISTURISING</text>
      <text class="product-title" x="24" y="128" font-size="30" letter-spacing="1.8">CREAM</text>
      <line class="title-rule" x1="24" y1="146" x2="286" y2="146"/>
      <text class="product-scent" x="24" y="182" font-size="21.5" letter-spacing="1.5">CITRUS &amp; GREEN TEA</text>
      <circle class="brand-mark" cx="178" cy="350" r="61" stroke-width="2.5"/>
      <text class="wordmark" transform="translate(220,1255) rotate(-90)" font-size="126" textLength="810" lengthAdjust="spacing">VELORENA</text>
      <rect class="volume-band" x="0" y="1280" width="343" height="75"/>
      <text class="volume-text" x="171" y="1327" font-size="24" text-anchor="middle">50ml / 1.7 Fl. Oz.</text>
    </g>
  </svg>

</main>
</body>
</html>
```